Gutscheinkarte aus Plastik
Zielgruppe
Fitnessbekleidung, Sportbekleidung, Funktionsbekleidung,Gym,Onlineshop,
Aufgabenstellung
Erstellen einer Gutscheinkarte aus Plastik für unseren neuen Onlineshop, die bei Bestellungen mit an die Kunden versendet wird.
-Maße: 86x54mm
-Farben: Schwarz und Neongrün(c0e200) evtl. noch eine dritte Farbe (wird Designer überlassen)
Folgender Text sollte vorhanden sein (Vorderseite):
Gutscheinwert: 10€
Gutscheincode: Ascend
Gültig: ab einem Bestellwert von 75€
Webadresse: www.ascend-now-sports.de
Unsere Marken: s. Anlage
Bitte Reihenfolge beigehalten + uvm.
Rückseite:
Versand in folgende Länder (evtl mit Länderflaggen oder Europakarte mit Stecknadel in der Ländern):
Deutschland
Österreich
Frankreich
Italien
Großbritannien
Niederlande
Belgien
Bulgarien
Dänemark
Estland
Finnland
Griechenland
Irland
Lettland
Litauen
Luxemburg
Malta
Polen
Portugal
Rumänien
Schweden
Slowakei
Slowenien
Spanien
Tschechien
Ungarn
Zypern

```html
<!DOCTYPE html>
<html lang="de">
<head>
<meta charset="utf-8">
<title>Gutscheinkarte – Ascend</title>
<link href="https://fonts.googleapis.com/css2?family=Anton&display=swap" rel="stylesheet">
<style>
  :root {
    --neon: #c0e200;
    --ink: #222222;
    --white: #ffffff;
    --backdrop: #e4e4e4;
  }
  html, body {
    margin: 0;
    width: 1200px;
    height: 848px;
    overflow: hidden;
    background: var(--backdrop);
    font-family: "Anton", "Arial Narrow", sans-serif;
  }
  .stage { position: relative; width: 1200px; height: 848px; }
  .card {
    position: absolute;
    width: 608px;
    height: 380px;
    box-shadow: 0 14px 24px rgba(0,0,0,0.3);
  }
  .card svg { display: block; width: 608px; height: 380px; }
  .card--front { left: 66px; top: 63px; }
  .card--back { left: 505px; top: 408px; }
  .side-label {
    position: absolute;
    writing-mode: vertical-rl;
    font-size: 66px;
    line-height: 1;
    letter-spacing: 1px;
  }
  .side-label--front { left: 674px; top: 62px; color: var(--neon); }
  .side-label--back { left: 1110px; top: 404px; color: var(--ink); }
  .t-neon { fill: var(--neon); }
  .t-ink { fill: var(--ink); }
  .t-white { fill: var(--white); }
  svg text { font-family: "Anton", "Arial Narrow", sans-serif; }
</style>
</head>
<body>
<div class="stage">

  <section class="card card--front" aria-label="Vorderseite">
    <svg viewBox="0 0 608 380">
      <rect class="t-ink" width="608" height="380"/>
      <text class="t-neon voucher-value" x="305" y="173" font-size="170" text-anchor="middle" textLength="222" lengthAdjust="spacingAndGlyphs">10€</text>
      <text class="t-neon voucher-code" x="317" y="197" font-size="20" text-anchor="middle">Gutscheincode: Ascend</text>
      <text class="t-neon voucher-terms" x="317" y="224" font-size="20" text-anchor="middle">Gültig: Ab einem Bestellwert von 75€</text>
      <polygon class="t-neon url-band" points="0,242 586,242 608,205 608,294 28,294 0,337"/>
      <text class="t-ink shop-url" x="312" y="286" font-size="46" text-anchor="middle" textLength="512" lengthAdjust="spacingAndGlyphs">www.ascend-now-sports.de</text>
      <g class="brand-row t-white" font-size="20" text-anchor="middle">
        <text x="90" y="340">Ironhall</text>
        <text x="176" y="340">Stridewear</text>
        <text x="287" y="340">Apex Wear</text>
        <text x="418" y="340">Vantage</text>
        <text x="526" y="340">Sunforge</text>
      </g>
    </svg>
  </section>
  <div class="side-label side-label--front">FRONT</div>

  <section class="card card--back" aria-label="Rückseite">
    <svg viewBox="0 0 608 380">
      <rect class="t-neon" width="608" height="380"/>
      <polygon class="t-ink heading-band" points="0,28 588,28 608,2 608,109 25,109 0,148"/>
      <text class="t-neon shipping-heading" x="312" y="94" font-size="48" text-anchor="middle" textLength="550" lengthAdjust="spacingAndGlyphs">Versand in folgende Länder</text>
      <g class="country-list t-ink" font-size="24" text-anchor="middle">
        <text x="295" y="139">Deutschland · Österreich · Frankreich</text>
        <text x="295" y="169">Italien · Großbritannien · Niederlande</text>
        <text x="295" y="198">Belgien · Bulgarien · Dänemark</text>
        <text x="295" y="228">Estland · Finnland · Griechenland · Irland</text>
        <text x="295" y="258">Lettland · Litauen · Luxemburg · Malta</text>
        <text x="295" y="288">Polen · Portugal · Rumänien · Schweden</text>
        <text x="295" y="318">Slowakei · Slowenien · Spanien</text>
        <text x="295" y="347">Tschechien · Ungarn · Zypern</text>
      </g>
    </svg>
  </section>
  <div class="side-label side-label--back">BACK</div>

</div>
</body>
</html>
```